Harborline Optical -Window Poster (Optometrist)

We are an optometry practice and we need a poster for a new store promotion for our window highlighting we now also sell 2 pairs of glasses as a package deal. The size will be 1300mm width x 1900mm height

The artwork will be displayed as a fabric banner in our shop window. We have 7 other banners with different services our business provides. The words needs to standout for passers by and the cars stopped at the traffic lights out front of our business. We already have signs with our logos phone number etc. so we won't need them included in the poster.

It would need to include the following information.

Two pair packages now available*

*Conditions apply
Updates

The artwork will be displayed as a fabric banner in our shop window. We have 7 other banners with different services our business provides. The words needs to standout for passers by and the cars stopped at the traffic lights out front of our business. We already have signs with our logos phone number etc. so we won't need them included in the poster. Thank you for your work it's amazing Added Saturday, February 18, 2017

The artwork will be displayed as a fabric banner in our shop window. We have 7 other banners with different services our business provides. The words needs to standout for passers by and the cars stopped at the traffic lights out front of our business. We already have signs with our logos phone number etc. so we won't need them included in the poster. Added Saturday, February 18, 2017

Target Market(s)

Cars driving past and stopped at traffic lights outside our store.

Industry/Entity Type

Optician

Requirements
Must have
• Poster must say:
• Two pair packages now available*
• *Conditions apply

```html
<!DOCTYPE html>
<html lang="en">
<head>
<meta charset="utf-8">
<title>Harborline Optical – Two Pair Packages Window Poster</title>
<link rel="stylesheet" href="https://fonts.googleapis.com/css2?family=Jost:wght@300;400;500;700&display=swap">
<style>
  :root {
    --stage: #b9bdc0;
    --poster-bg: #f1f3f5;
    --poster-border: #ffffff;
    --navy: #1d3f97;
    --royal: #1f5fbf;
    --cyan: #20b4ea;
    --cyan-light: #5fd0f5;
    --orange: #f58a1f;
    --ink-fine: #3a3f48;
    --photo-warm: #d9b98f;
    --photo-light: #eef0f2;
  }
  * { margin: 0; padding: 0; box-sizing: border-box; }
  html, body {
    width: 1200px; height: 869px; overflow: hidden;
    background: var(--stage);
    font-family: "Jost", "Futura", sans-serif;
  }
  .stage { position: relative; width: 1200px; height: 869px; }
  .poster {
    position: absolute; top: 84px;
    width: 479px; height: 700px;
    background: linear-gradient(180deg, #fafbfc 0%, var(--poster-bg) 100%);
    border: 8px solid var(--poster-border);
    overflow: hidden;
    box-shadow: 0 6px 18px rgba(0,0,0,0.18);
  }
  .poster--ribbon { left: 81px; }
  .poster--badge { left: 640px; }
  .poster__corner { position: absolute; top: 0; left: 0; width: 100%; height: 90px; }
  .poster__headline {
    position: absolute; top: 78px; left: 0; width: 100%;
    text-align: center; line-height: 1;
  }
  .headline__lead {
    display: block; font-weight: 700; font-size: 60px; letter-spacing: 1px;
    background: linear-gradient(180deg, var(--cyan-light) 0%, var(--cyan) 55%, var(--royal) 100%);
    -webkit-background-clip: text; background-clip: text; color: transparent;
  }
  .headline__sub {
    display: block; font-weight: 300; font-size: 61px; color: var(--navy);
    margin-top: -2px; letter-spacing: 0.5px;
  }
  .poster__photo {
    position: absolute; left: 96px; top: 212px; width: 375px; height: 444px;
    background: radial-gradient(ellipse at 50% 35%, var(--photo-warm) 0%, #e4d2bb 40%, var(--photo-light) 75%);
  }
  .poster__ribbon { position: absolute; left: 34px; top: 236px; width: 170px; height: 170px; }
  .poster__badge {
    position: absolute; left: 28px; top: 236px; width: 160px; height: 160px;
    border-radius: 50%;
    background: radial-gradient(circle at 40% 35%, var(--cyan-light) 0%, var(--cyan) 45%, var(--royal) 100%);
    box-shadow: 0 0 0 4px rgba(255,255,255,0.9);
    color: #fff; text-align: center;
    display: flex; flex-direction: column; justify-content: center; align-items: center;
  }
  .badge__now { font-weight: 300; font-size: 46px; line-height: 1; }
  .badge__available { font-weight: 400; font-size: 17px; letter-spacing: 1px; margin-top: 2px; }
  .poster__conditions {
    position: absolute; left: 14px; bottom: 34px;
    font-size: 9px; color: var(--ink-fine);
  }
  .poster__base { position: absolute; left: 0; bottom: 0; width: 100%; height: 34px; }
</style>
</head>
<body>
<main class="stage">

  <section class="poster poster--ribbon">
    <svg class="poster__corner" viewBox="0 0 463 90" preserveAspectRatio="none" aria-hidden="true">
      <polygon points="0,0 463,0 463,40 250,28" fill="var(--cyan)"/>
      <polygon points="0,0 200,0 60,40 0,48" fill="var(--navy)"/>
    </svg>
    <h1 class="poster__headline">
      <span class="headline__lead">TWO PAIR</span>
      <span class="headline__sub">PACKAGES</span>
    </h1>
    <div class="poster__photo" role="img" aria-label="Photo of a smiling child in large glasses reading a book"></div>
    <svg class="poster__ribbon" viewBox="0 0 170 170" aria-label="Now available">
      <polygon points="10,5 150,20 130,30 150,40 10,40" fill="var(--navy)"/>
      <polygon points="0,38 140,48 136,84 4,74" fill="var(--orange)"/>
      <text x="70" y="70" text-anchor="middle" font-family="Jost, sans-serif" font-weight="500" font-size="24" fill="#fff" transform="rotate(4 70 62)">NOW</text>
      <polygon points="14,96 160,86 164,122 18,132" fill="var(--orange)"/>
      <text x="89" y="117" text-anchor="middle" font-family="Jost, sans-serif" font-weight="500" font-size="20" fill="#fff" transform="rotate(-4 89 110)">AVAILABLE</text>
      <polygon points="20,130 160,122 160,160 20,160 40,145" fill="var(--navy)"/>
    </svg>
    <p class="poster__conditions">*Conditions apply</p>
    <svg class="poster__base" viewBox="0 0 463 34" preserveAspectRatio="none" aria-hidden="true">
      <rect x="0" y="4" width="463" height="10" fill="var(--cyan)"/>
      <rect x="0" y="14" width="463" height="20" fill="var(--navy)"/>
    </svg>
  </section>

  <section class="poster poster--badge">
    <svg class="poster__corner" viewBox="0 0 463 90" preserveAspectRatio="none" aria-hidden="true">
      <polygon points="0,0 463,0 463,40 250,28" fill="var(--cyan)"/>
      <polygon points="0,0 200,0 60,40 0,48" fill="var(--navy)"/>
    </svg>
    <h1 class="poster__headline">
      <span class="headline__lead">TWO PAIR</span>
      <span class="headline__sub">PACKAGES</span>
    </h1>
    <div class="poster__photo" role="img" aria-label="Photo of a smiling child in large glasses reading a book"></div>
    <div class="poster__badge">
      <span class="badge__now">NOW</span>
      <span class="badge__available">AVAILABLE*</span>
    </div>
    <p class="poster__conditions">*Conditions apply</p>
    <svg class="poster__base" viewBox="0 0 463 34" preserveAspectRatio="none" aria-hidden="true">
      <rect x="0" y="4" width="463" height="10" fill="var(--cyan)"/>
      <rect x="0" y="14" width="463" height="20" fill="var(--navy)"/>
    </svg>
  </section>

</main>
</body>
</html>
```